Crestwell Renewal Business Card Design Phase 2

Professional and clean design. The design colors should flow with the logo. Two-sided card with the website on the back which is:

www.CrestwellRenewal.example.

"Specializing in Water Damage Restoration"

On the front I need the name, email, phone, and logo.

Name: Dorian Halvek
Email: Dorian@CrestwellRenewal.example
Phone: 555-318-2046 for now

I only have the Preview and Thumbnail right now but should have the source files uploaded within a day or two.

Target Market(s)

Flood victims, home owners with water damage from busted pipes etc...

Industry/Entity Type

Business

Contact Information for Business Card

Name: Dorian Halvek

Font styles to use
Serif
Sans Serif

Requirements
Must have
• Business Card Details Info

```html
<!DOCTYPE html>
<html lang="en">
<head>
<meta charset="utf-8">
<title>Crestwell Renewal Business Card</title>
<link rel="stylesheet" href="https://fonts.googleapis.com/css2?family=PT+Sans:ital,wght@0,400;0,700;1,400;1,700&display=swap">
<style>
  :root {
    --navy: #1f3865;
    --green: #4b8d3b;
    --white: #ffffff;
    --ink: #3d4450;
    --backdrop: #e9ebee;
    --rule: #8a9ab8;
    --soft: #c9d2e3;
  }
  * { box-sizing: border-box; margin: 0; padding: 0; }
  html, body { width: 1105px; height: 1200px; overflow: hidden; }
  body {
    background: var(--backdrop);
    font-family: "PT Sans", Arial, sans-serif;
    position: relative;
  }
  .card {
    position: absolute;
    left: 192px;
    width: 721px;
    height: 412px;
    overflow: hidden;
  }
  .card--front { top: 146px; background: var(--white); box-shadow: 0 0 0 1px #d5d9df; }
  .card--back { top: 602px; background: var(--navy); }
  .card__shapes { position: absolute; inset: 0; }
  .brand {
    position: absolute;
    right: 36px;
    top: 60px;
    display: flex;
    align-items: center;
    gap: 14px;
    color: var(--navy);
    font-weight: 700;
    font-size: 34px;
    line-height: 1.1;
    text-align: right;
  }
  .brand__mark {
    width: 22px;
    height: 22px;
    background: var(--navy);
    flex: none;
  }
  .contact { position: absolute; left: 39px; top: 207px; color: var(--ink); }
  .contact__name { color: var(--navy); font-size: 27px; font-weight: 700; margin-bottom: 12px; }
  .contact__row { display: flex; align-items: center; gap: 10px; font-size: 19px; height: 31px; }
  .contact__icon { width: 18px; height: 18px; fill: var(--navy); flex: none; }
  .tagline {
    font-style: italic;
    font-weight: 700;
    color: var(--navy);
    font-size: 18px;
    margin-top: 7px;
  }
  .scene {
    position: absolute;
    left: 198px;
    top: 74px;
    width: 340px;
    height: 226px;
    border-radius: 6px;
    background: radial-gradient(ellipse at center, rgba(255,255,255,0.55), rgba(255,255,255,0.12) 70%, rgba(255,255,255,0));
  }
  .back-tagline {
    position: absolute;
    left: 0; right: 0;
    top: 330px;
    display: flex;
    align-items: center;
    justify-content: center;
    gap: 8px;
    color: var(--white);
    font-style: italic;
    font-size: 19px;
  }
  .back-tagline::before, .back-tagline::after {
    content: "";
    height: 1px;
    background: var(--rule);
  }
  .back-tagline::before { width: 118px; }
  .back-tagline::after { width: 90px; }
  .back-website {
    position: absolute;
    left: 0; right: 0;
    top: 364px;
    text-align: center;
    color: var(--soft);
    font-size: 17px;
    letter-spacing: 0.3px;
  }
</style>
</head>
<body>
  <section class="card card--front" aria-label="Front of business card">
    <svg class="card__shapes" viewBox="0 0 721 412" width="721" height="412" aria-hidden="true">
      <path d="M0 0 H160 Q40 40 0 165 Z" fill="var(--navy)"/>
      <path d="M160 0 Q36 34 4 168" fill="none" stroke="var(--green)" stroke-width="5"/>
      <path d="M721 250 Q690 360 556 412 H721 Z" fill="var(--navy)"/>
      <path d="M717 244 Q688 360 552 412" fill="none" stroke="var(--green)" stroke-width="5"/>
    </svg>
    <div class="brand">
      <span class="brand__mark" aria-hidden="true"></span>
      <span class="brand__name">Crestwell<br>Renewal</span>
    </div>
    <div class="contact">
      <p class="contact__name">Dorian Halvek</p>
      <p class="contact__row">
        <svg class="contact__icon" viewBox="0 0 24 24"><path d="M6.6 10.8a15 15 0 0 0 6.6 6.6l2.2-2.2c.3-.3.7-.4 1-.2 1.1.4 2.3.6 3.6.6.6 0 1 .4 1 1V20c0 .6-.4 1-1 1A17 17 0 0 1 3 4c0-.6.4-1 1-1h3.5c.6 0 1 .4 1 1 0 1.3.2 2.5.6 3.6.1.3 0 .7-.2 1z"/></svg>
        555-318-2046
      </p>
      <p class="contact__row">
        <svg class="contact__icon" viewBox="0 0 24 24"><path d="M2 5h20v14H2z M2 5l10 8 10-8" fill="var(--navy)" stroke="var(--white)" stroke-width="1.5"/></svg>
        Dorian@CrestwellRenewal.example
      </p>
      <p class="contact__row">
        <svg class="contact__icon" viewBox="0 0 24 24"><circle cx="12" cy="12" r="10"/><path d="M7 8c2 0 3 1 3 3s2 2 2 4-1 3-1 4M15 5c0 2 2 2 3 4" fill="none" stroke="var(--white)" stroke-width="1.5"/></svg>
        www.CrestwellRenewal.example
      </p>
      <p class="tagline">Specializing in Water Damage Restoration</p>
    </div>
  </section>

  <section class="card card--back" aria-label="Back of business card">
    <div class="scene" role="img" aria-label="Illustration of a flooded house with a restoration worker pumping out water"></div>
    <p class="back-tagline">Specializing in Water Damage Restoration</p>
    <p class="back-website">www.CrestwellRenewal.example</p>
  </section>
</body>
</html>
```